Business card for psychiatrist

Business card design project for a psychiatristWe would like to have the impression of 1. We (patient and the doctor) are working together.2. Light the way so that patients can see where they are going and what their goals are.3. One side of the business card will have the letter "TFP" which stands for Thornvale Family Psychiatry.4. The other side of the business card will have the address, phone number, name of the psychiatrist, website, etc.5. A logo could go into either side of the business card. Let's see what looks better.
Business card design project for a psychiatrist
We would like to have the impression of
1. We (patient and the doctor) are working together.
2. Light the way so that patients can see where they are going and what their goals are.
3. One side of the business card will have the letter "TFP" which stands for Thornvale Family Psychiatry.
4. The other side of the business card will have the address, phone number, name of the psychiatrist, website, etc.
5. A logo could go into either side of the business card. Let's see what looks better.
Colors
Designer to choose colors to be used in the design.
Look and feel
Each slider illustrates characteristics of the customer's brand and the style your logo design should communicate.

```html
<!DOCTYPE html>
<html lang="en">
<head>
<meta charset="utf-8">
<title>Thornvale Family Psychiatry – Business Card</title>
<link rel="stylesheet" href="https://fonts.googleapis.com/css2?family=Open+Sans:wght@400;700&family=Arimo:wght@400&display=swap">
<style>
  :root {
    --backdrop: #2a2a2c;
    --card: #121212;
    --card-edge: #1c1c1c;
    --accent: #29a8e2;
    --text-soft: #a9a9a9;
    --divider: #5a5a5a;
  }
  * { margin: 0; padding: 0; box-sizing: border-box; }
  html, body {
    width: 1200px; height: 900px; overflow: hidden;
    background: var(--backdrop);
  }
  .stage {
    width: 1200px; height: 900px;
    display: flex; flex-direction: column; align-items: center; justify-content: center;
    gap: 44px;
  }
  .card {
    position: relative;
    width: 560px; height: 320px;
    background: radial-gradient(ellipse at 40% 35%, var(--card-edge), var(--card) 75%);
    box-shadow: 0 14px 30px rgba(0,0,0,0.45);
    overflow: hidden;
  }
  .card__band {
    position: absolute; left: 0; right: 0; bottom: 0;
    height: 9px; background: var(--accent);
  }
  /* Front */
  .brand {
    position: absolute; left: 0; right: 0; top: 112px;
    display: flex; align-items: center; justify-content: center; gap: 14px;
  }
  .brand__dot {
    width: 26px; height: 26px; border-radius: 50%;
    background: var(--accent);
  }
  .brand__name {
    font-family: "Open Sans", sans-serif; font-weight: 700;
    font-size: 30px; letter-spacing: 1px; text-transform: uppercase;
    color: var(--accent); line-height: 1.15; text-align: left;
  }
  /* Back */
  .person {
    position: absolute; left: 86px; top: 104px; width: 170px;
    font-family: "Arimo", sans-serif;
  }
  .person__name {
    font-family: "Open Sans", sans-serif; font-weight: 700;
    font-size: 19px; color: var(--accent); text-transform: uppercase;
  }
  .person__role { font-size: 14px; color: var(--text-soft); margin-top: 2px; }
  .divider {
    position: absolute; left: 272px; top: 100px;
    width: 1px; height: 78px; background: var(--divider);
  }
  .contacts {
    position: absolute; left: 292px; top: 100px;
    list-style: none;
    font-family: "Arimo", sans-serif; font-size: 15px; color: var(--text-soft);
  }
  .contacts li { display: flex; align-items: center; gap: 9px; height: 20px; }
  .contacts svg { width: 12px; height: 12px; fill: var(--accent); flex: none; }
  .address {
    position: absolute; left: 86px; top: 222px;
    font-family: "Arimo", sans-serif; font-size: 15px; color: var(--text-soft);
  }
</style>
</head>
<body>
<main class="stage">
  <section class="card card--front">
    <div class="brand">
      <span class="brand__dot"></span>
      <span class="brand__name">Thornvale<br>Family Psychiatry</span>
    </div>
    <div class="card__band"></div>
  </section>

  <section class="card card--back">
    <div class="person">
      <p class="person__name">Daniel Marsh</p>
      <p class="person__role">Managing Director</p>
    </div>
    <div class="divider"></div>
    <ul class="contacts">
      <li>
        <svg viewBox="0 0 12 12"><path d="M1 4c0-2 2-3 5-3s5 1 5 3l-2 1-1-2H4L3 5 1 4zM2 6h8l1 5H1z"/></svg>
        044-310 772 418
      </li>
      <li>
        <svg viewBox="0 0 12 12"><path d="M3 0h6v12H3zM4 1.5v8h4v-8z"/></svg>
        044-310 772 418
      </li>
      <li>
        <svg viewBox="0 0 12 12"><path d="M0 2h12v8H0zM1 3l5 4 5-4v-.2H1z"/></svg>
        hello@thornvalefp.com
      </li>
      <li>
        <svg viewBox="0 0 12 12"><circle cx="6" cy="6" r="5.5"/></svg>
        www.thornvalefp.com
      </li>
    </ul>
    <p class="address">48 Linden Row, Thornvale Heights, Marlow County, 204518.</p>
    <div class="card__band"></div>
  </section>
</main>
</body>
</html>
```